Business Card

We need some ideas for corporate business cards. I'm interested in a double sided card, with one side featuring our corporate logo, the other side with employee information.

Corporate colors, logo etc. available at www.brivalo.com

Industry/Entity Type

Business

Requirements
Must have
• The "Brivalo" logo with stylized "O"

Nice to have
• Preferred font is calibri

```html
<!DOCTYPE html>
<html lang="en">
<head>
<meta charset="utf-8">
<title>Brivalo Business Card</title>
<link rel="stylesheet" href="https://fonts.googleapis.com/css2?family=Carlito:wght@400;700&display=swap">
<style>
  :root {
    --teal: #0f6e6c;
    --teal-deep: #0b5d5b;
    --teal-soft: #3f8f8c;
    --paper: #f1f1ef;
    --ink-light: #e9f3f2;
    --backdrop: #d9d6d4;
  }
  * { margin: 0; padding: 0; box-sizing: border-box; }
  html, body {
    width: 1200px;
    height: 900px;
    overflow: hidden;
    background: var(--backdrop);
    font-family: "Carlito", "Calibri", sans-serif;
  }
  .canvas {
    position: relative;
    width: 1200px;
    height: 900px;
  }
  .card {
    position: absolute;
    width: 560px;
    height: 320px;
    border-radius: 4px;
    overflow: hidden;
    box-shadow: 0 14px 30px rgba(40, 30, 30, 0.22);
  }
  /* Back side */
  .card-back {
    left: 580px;
    top: 110px;
    background: var(--teal);
  }
  .card-back .pattern-area {
    position: absolute;
    inset: 0;
    background: radial-gradient(circle at 50% 50%, var(--teal-soft) 0%, var(--teal) 70%);
  }
  /* Front side */
  .card-front {
    left: 60px;
    top: 470px;
    background: var(--paper);
    display: flex;
  }
  .edge-band {
    width: 14px;
    background: var(--teal);
  }
  .brand-area {
    flex: 1;
    display: flex;
    align-items: center;
    padding-left: 44px;
  }
  .brand-name {
    font-weight: 700;
    font-size: 52px;
    letter-spacing: 9px;
    color: var(--teal);
    text-transform: uppercase;
  }
  .info-panel {
    width: 196px;
    background: var(--teal);
    color: var(--ink-light);
    font-weight: 400;
    font-size: 13.5px;
    line-height: 1.3;
    padding: 50px 20px 0 30px;
  }
  .info-block { margin-bottom: 14px; }
</style>
</head>
<body>
  <main class="canvas">
    <section class="card card-back" aria-label="Card back">
      <div class="pattern-area" role="img" aria-label="Repeating brand symbol pattern in light teal on teal, with one white symbol at the centre"></div>
    </section>

    <section class="card card-front" aria-label="Card front">
      <div class="edge-band"></div>
      <div class="brand-area">
        <span class="brand-name">Brivalo</span>
      </div>
      <div class="info-panel">
        <p class="info-block">Name Here<br>Post</p>
        <p class="info-block">Halvane Studio<br>Merelstraat 48<br>2140 Lindvoort</p>
        <p class="info-block">T : 03/ 418.27.64<br>www.halvane.be</p>
      </div>
    </section>
  </main>
</body>
</html>
```